New Business Card Design Project

I need a design for business cards, i am an electrical business called "Tandor Electrical and Communications" i need the cards to be double sided with the company logo on the back (attached) the front needs to say my company name, web site, email address, telephone number, and ABN number and electrical license number. I am open to different arrangements of the information but would like the background to be incorporating something electrical or something that looks smart. open to all additional ideas also.

The company colours are orange and grey see logo attached.

Business Name: Tandor Electrical and Communications
Website: tandorelectricalandcomms.example.au
Email: brent@tandorelectricalandcomms.example.au
Telephone(mobile): 0481203967
ABN: 71829034618
Lic No: 830472F

Target Market(s)

Business entities, Project Managers, Accounts, Clients

Industry/Entity Type

Electrician

Contact Information for Business Card

I need a design for business cards, i am an electrical business called "Tandor Electrical and Communications" i need the cards to be double sided with the company logo on the back (attached) the front needs to say my company name

Font styles to use
Serif
Sans Serif

Colors
f37122
5c5c5c

Requirements
Must have
• Must have the Logo on the back open to different ways of it being on the back but had in mind to keep it central but again open to other options
Nice to have
• A real modern cool background that is eye catching yet contemporary
Should not have
• No backgrounds of a light bulb or plug or anything like that

```html
<!DOCTYPE html>
<html lang="en">
<head>
<meta charset="utf-8">
<title>Tandor Electrical and Communications – Business Cards</title>
<link rel="stylesheet" href="https://fonts.googleapis.com/css2?family=Didact+Gothic&family=Montserrat:wght@600&display=swap">
<style>
  :root {
    --backdrop: #2a2a2a;
    --card-white: #f7f7f7;
    --card-grey: #4a4a4c;
    --brand-grey: #5c5c5c;
    --brand-orange: #f3a122;
    --accent-orange: #f37122;
    --text-light: #e6e6e6;
  }
  * { box-sizing: border-box; margin: 0; padding: 0; }
  html, body {
    width: 1200px; height: 997px; overflow: hidden;
    background: var(--backdrop);
    font-family: "Didact Gothic", sans-serif;
  }
  .stage { position: relative; width: 1200px; height: 997px; }
  .card {
    position: absolute;
    width: 540px; height: 310px;
    border-radius: 22px;
    overflow: hidden;
    box-shadow: 0 18px 40px rgba(0,0,0,.55);
  }
  .card-back { left: 80px; top: 130px; }
  .card-front { left: 580px; top: 500px; }
  .card-bg { position: absolute; inset: 0; width: 100%; height: 100%; }
  .logo {
    position: absolute;
    display: flex; flex-direction: column; align-items: flex-start;
  }
  .logo-row { display: flex; align-items: center; gap: 12px; }
  .logo-dot {
    width: 20px; height: 20px; border-radius: 50%;
    background: var(--brand-orange);
  }
  .logo-name {
    font-family: "Didact Gothic", sans-serif;
    font-size: 64px; letter-spacing: 4px; line-height: 1;
    color: var(--brand-grey);
    text-transform: uppercase;
  }
  .logo-tagline {
    margin-top: 6px; margin-left: 34px;
    font-size: 15px; letter-spacing: 1.5px;
    color: var(--brand-orange);
    text-transform: uppercase;
  }
  .card-back .logo { left: 70px; top: 70px; }
  .website {
    position: absolute; right: 36px; bottom: 30px;
    font-size: 17px; letter-spacing: 2px;
    color: var(--brand-orange);
  }
  .card-front .logo { left: 60px; top: 38px; }
  .registration {
    position: absolute; left: 128px; top: 142px;
    font-size: 12px; letter-spacing: .5px;
    color: var(--brand-grey);
  }
  .registration span + span { margin-left: 14px; }
  .contact {
    position: absolute; right: 26px; top: 190px;
    list-style: none; text-align: right;
    font-size: 12px; line-height: 22px;
    color: var(--text-light);
  }
  .contact li { display: flex; justify-content: flex-end; align-items: center; gap: 8px; }
  .contact svg { width: 11px; height: 11px; fill: var(--brand-orange); }
  .holder { position: absolute; left: 30px; bottom: 22px; }
  .holder-name {
    font-family: "Montserrat", sans-serif; font-weight: 600;
    font-size: 20px; color: var(--brand-orange);
  }
  .holder-role { font-size: 14px; color: var(--text-light); }
  .holder-company { font-size: 13px; letter-spacing: .5px; color: var(--brand-orange); }
</style>
</head>
<body>
<main class="stage">

  <section class="card card-back" aria-label="Card back">
    <svg class="card-bg" viewBox="0 0 540 310" preserveAspectRatio="none" aria-hidden="true">
      <rect width="540" height="310" fill="var(--card-white)"/>
      <path d="M0,262 C200,250 400,160 540,28 L540,310 L0,310 Z" fill="var(--card-grey)"/>
      <path d="M0,262 C200,250 400,160 540,28" fill="none" stroke="var(--brand-orange)" stroke-width="4"/>
    </svg>
    <div class="logo">
      <div class="logo-row"><span class="logo-dot"></span><span class="logo-name">Tandor</span></div>
      <div class="logo-tagline">Electrical &amp; Communications</div>
    </div>
    <p class="website">www.tandorelectricalandcomms.example.au</p>
  </section>

  <section class="card card-front" aria-label="Card front">
    <svg class="card-bg" viewBox="0 0 540 310" preserveAspectRatio="none" aria-hidden="true">
      <rect width="540" height="310" fill="var(--card-white)"/>
      <path d="M0,200 C220,200 420,150 540,80 L540,310 L0,310 Z" fill="var(--card-grey)"/>
      <path d="M0,200 C220,200 420,150 540,80" fill="none" stroke="var(--brand-orange)" stroke-width="4"/>
    </svg>
    <div class="logo">
      <div class="logo-row"><span class="logo-dot"></span><span class="logo-name">Tandor</span></div>
      <div class="logo-tagline">Electrical &amp; Communications</div>
    </div>
    <p class="registration"><span>Lic No: 830472F</span><span>ABN: 71829034618</span></p>
    <ul class="contact">
      <li>0481203967
        <svg viewBox="0 0 24 24" aria-hidden="true"><path d="M6.6 10.8a15 15 0 0 0 6.6 6.6l2.2-2.2a1 1 0 0 1 1-.25 11.4 11.4 0 0 0 3.6.57 1 1 0 0 1 1 1V20a1 1 0 0 1-1 1A17 17 0 0 1 3 4a1 1 0 0 1 1-1h3.5a1 1 0 0 1 1 1c0 1.25.2 2.45.57 3.6a1 1 0 0 1-.25 1z"/></svg>
      </li>
      <li>brent@tandorelectricalandcomms.example.au
        <svg viewBox="0 0 24 24" aria-hidden="true"><path d="M2 5h20v14H2z M2 5l10 8 10-8" /></svg>
      </li>
    </ul>
    <div class="holder">
      <p class="holder-name">Brent D</p>
      <p class="holder-role">Owner</p>
      <p class="holder-company">Tandor Electrical &amp; Communications</p>
    </div>
  </section>

</main>
</body>
</html>
```